We have a new logo so we need to change our business card

We're super Happy with our current cards but I think with a new logo should come a new design. I wouldn't mind seeing the icons that we used on the back last time reused on this card. Please feel free to visit our website to get a sense for our brand www.brindlewick.ca

I need the final final to have contact info for:

Gordon Hasley
Co-Owner
info@brindlewick.ca
778-315-6207

and

Marjorie Hasley
Co-Owner
info@brindlewick.ca
778-342-5810

Target Market(s)

Female dog owners, 21 to 70

Industry/Entity Type

pet industry

Contact Information for Business Card

included in brief

Requirements
Should not have
• We do not want it to look cartonish

```html
<!DOCTYPE html>
<html lang="en">
<head>
<meta charset="utf-8">
<title>Brindlewick Business Card</title>
<link href="https://fonts.googleapis.com/css2?family=Montserrat:wght@400;500;700;800&display=swap" rel="stylesheet">
<style>
  :root {
    --bg: #9b9b9b;
    --card: #222222;
    --green: #8fd35f;
    --green-dark: #5f9440;
    --white: #f2f2f2;
    --muted: #c9c9c9;
    --badge: #6e7370;
    --badge-light: #c8d4d8;
  }
  * { box-sizing: border-box; margin: 0; padding: 0; }
  html, body { width: 1200px; height: 1050px; overflow: hidden; }
  body {
    background: var(--bg);
    font-family: "Montserrat", Arial, sans-serif;
    color: var(--white);
    position: relative;
  }
  .card {
    position: absolute;
    left: 220px;
    width: 760px;
    height: 434px;
    background: var(--card);
    border-bottom: 6px solid var(--green);
    box-shadow: 0 18px 40px rgba(0,0,0,0.35);
  }
  .card-front { top: 60px; }
  .card-back { top: 556px; }

  /* Front */
  .front-brand {
    position: absolute;
    left: 80px; top: 150px;
    display: flex; align-items: center; gap: 18px;
  }
  .brand-dot {
    width: 110px; height: 110px; border-radius: 50%;
    background: var(--green);
  }
  .brand-name {
    font-weight: 700; font-size: 34px; color: var(--green);
  }
  .front-contact {
    position: absolute;
    left: 430px; top: 110px;
  }
  .person-name {
    font-weight: 700; font-size: 30px; color: var(--green);
    letter-spacing: 0.5px;
  }
  .person-role {
    font-size: 17px; color: var(--white); margin-top: 4px; margin-bottom: 30px;
  }
  .contact-line {
    display: flex; align-items: center; gap: 12px;
    font-size: 17px; margin-bottom: 14px;
  }
  .contact-icon {
    width: 26px; height: 26px; border-radius: 50%;
    background: var(--green);
    display: flex; align-items: center; justify-content: center;
  }

  /* Back */
  .back-brand {
    text-align: center; padding-top: 34px;
  }
  .back-brand .brand-name { font-size: 52px; color: var(--green-dark); }
  .tagline {
    font-weight: 700; font-size: 17px; letter-spacing: 9px;
    color: var(--green-dark); margin-top: 6px;
  }
  .benefits-pill {
    display: inline-block; margin-top: 16px;
    background: var(--green); color: #1a1a1a;
    font-weight: 800; font-size: 17px; letter-spacing: 1px;
    padding: 4px 16px; border-radius: 8px;
  }
  .benefit-list {
    text-align: center; font-size: 15px; line-height: 1.45;
    margin-top: 10px; color: var(--white);
  }
  .tick {
    display: inline-block; vertical-align: -2px; margin: 0 4px;
  }
  .badge-row {
    position: absolute; left: 50px; right: 50px; bottom: 24px;
    display: flex; justify-content: space-between;
  }
  .badge {
    width: 82px; height: 82px; border-radius: 50%;
    background: var(--badge);
    border: 4px solid var(--badge-light);
  }
</style>
</head>
<body>

<section class="card card-front">
  <div class="front-brand">
    <div class="brand-dot"></div>
    <span class="brand-name">Brindlewick</span>
  </div>
  <div class="front-contact">
    <h1 class="person-name">GORDON HASLEY</h1>
    <p class="person-role">Co-Owner</p>
    <p class="contact-line">
      <span class="contact-icon"><svg width="14" height="14" viewBox="0 0 24 24"><path fill="#222" d="M6.6 10.8a15 15 0 0 0 6.6 6.6l2.2-2.2c.3-.3.7-.4 1-.2 1.1.4 2.3.6 3.6.6.6 0 1 .4 1 1V20c0 .6-.4 1-1 1A17 17 0 0 1 3 4c0-.6.4-1 1-1h3.5c.6 0 1 .4 1 1 0 1.3.2 2.5.6 3.6.1.3 0 .7-.2 1z"/></svg></span>
      778-315-6207
    </p>
    <p class="contact-line">
      <span class="contact-icon"><svg width="14" height="14" viewBox="0 0 24 24"><rect x="3" y="6" width="18" height="12" fill="#222"/><path d="M3 6l9 7 9-7" stroke="#8fd35f" stroke-width="1.6" fill="none"/></svg></span>
      info@brindlewick.ca
    </p>
    <p class="contact-line">
      <span class="contact-icon"><svg width="14" height="14" viewBox="0 0 24 24"><circle cx="12" cy="12" r="9" fill="none" stroke="#222" stroke-width="2.4"/><path d="M3 12h18M12 3c3 3 3 15 0 18M12 3c-3 3-3 15 0 18" stroke="#222" stroke-width="1.6" fill="none"/></svg></span>
      brindlewick.ca
    </p>
  </div>
</section>

<section class="card card-back">
  <div class="back-brand">
    <div class="brand-name">Brindlewick</div>
    <div class="tagline">THE FUR FRESHENER</div>
    <span class="benefits-pill">BENEFITS</span>
  </div>
  <div class="benefit-list">
    <p>Improves condition of the skin and fur</p>
    <p>Reduces shedding &amp; dandruff
      <svg class="tick" width="15" height="15" viewBox="0 0 16 16"><circle cx="8" cy="8" r="8" fill="#8fd35f"/><path d="M4.5 8.2l2.3 2.3 4.7-4.8" stroke="#222" stroke-width="2" fill="none"/></svg>
      Strengthens the immune system</p>
    <p>Helps eliminate unwanted odours
      <svg class="tick" width="15" height="15" viewBox="0 0 16 16"><circle cx="8" cy="8" r="8" fill="#8fd35f"/><path d="M4.5 8.2l2.3 2.3 4.7-4.8" stroke="#222" stroke-width="2" fill="none"/></svg>
      Adds a scented benefit</p>
    <p>Helps with; anxiety, arthritis, insomnia, drowsiness, skin irritation &amp; depression</p>
  </div>
  <div class="badge-row">
    <div class="badge"></div>
    <div class="badge"></div>
    <div class="badge"></div>
    <div class="badge"></div>
    <div class="badge"></div>
    <div class="badge"></div>
  </div>
</section>

</body>
</html>
```